Mina Vell makeup artist business cards

Hello
I need business cards for my freelance makeup artist business.

What I am looking for;
Sleek
Clear and easily read
Expensive/exclusive feel
Black and white
Embossed

Information that must be included on back
My name
My contact number
My email
My website
My Friendspace
My snapframe

If it works I'd like to also include on the back;
Bridal, glamour, evening, editorial, fashion, tv, film makeup
(Open to exclude if it makes the card look to busy)

Requirements
Must have
• My logo mina Vell makeup artist as shown in photos
Nice to have
• I'd like to see some designs with the social media icons (as shown in image attached)

```html
<!DOCTYPE html>
<html lang="en">
<head>
<meta charset="utf-8">
<title>Mina Vell – Makeup Artist Business Card</title>
<link rel="stylesheet" href="https://fonts.googleapis.com/css2?family=PT+Sans:ital,wght@0,400;1,700&family=Source+Sans+3:wght@400;500&display=swap">
<style>
  :root {
    --card-bg: #000000;
    --ink: #ffffff;
    --ink-soft: #f2f2f2;
  }
  * { margin: 0; padding: 0; box-sizing: border-box; }
  html, body {
    width: 1200px;
    height: 720px;
    overflow: hidden;
    background: var(--card-bg);
  }
  .card {
    position: relative;
    width: 1200px;
    height: 720px;
    background: var(--card-bg);
    color: var(--ink);
    font-family: "Source Sans 3", "PT Sans", sans-serif;
  }
  .brand-mark {
    position: absolute;
    left: 139px;
    top: 106px;
    width: 78px;
    height: 78px;
    border-radius: 50%;
    background: var(--ink-soft);
  }
  .brand-name {
    position: absolute;
    left: 247px;
    top: 98px;
    font-size: 55px;
    font-weight: 400;
    letter-spacing: 0.2em;
    line-height: 1;
    white-space: nowrap;
  }
  .brand-role {
    position: absolute;
    left: 249px;
    top: 162px;
    font-size: 23px;
    font-weight: 400;
    line-height: 1;
  }
  .divider {
    position: absolute;
    left: 95px;
    top: 208px;
    width: 838px;
    height: 2px;
    background: var(--ink);
  }
  .contact-list {
    list-style: none;
  }
  .contact-item {
    position: absolute;
    left: 100px;
    height: 40px;
    display: flex;
    align-items: center;
    font-size: 30px;
    line-height: 1;
  }
  .contact-item .icon {
    width: 38px;
    height: 38px;
    display: flex;
    align-items: center;
    justify-content: center;
    margin-right: 14px;
  }
  .contact-item .icon svg { display: block; }
  .item-phone   { top: 252px; }
  .item-email   { top: 330px; }
  .item-website { top: 408px; }
  .item-social-a { top: 485px; }
  .item-social-b { top: 560px; }
  .plain-dot {
    width: 28px; height: 28px; border-radius: 50%; background: var(--ink);
  }
  .plain-square {
    width: 29px; height: 29px; border-radius: 5px; background: var(--ink);
  }
  .specialties {
    position: absolute;
    left: 662px;
    top: 520px;
    font-family: "PT Sans", sans-serif;
    font-weight: 700;
    font-style: italic;
    font-variant: small-caps;
    font-size: 31px;
    line-height: 45px;
    color: var(--ink);
    text-shadow: 1px 1px 0 #555;
  }
</style>
</head>
<body>
  <main class="card">
    <div class="brand-mark" aria-hidden="true"></div>
    <h1 class="brand-name">MINA VELL</h1>
    <p class="brand-role">Makeup Artist</p>
    <div class="divider"></div>

    <ul class="contact-list">
      <li class="contact-item item-phone">
        <span class="icon">
          <svg width="26" height="26" viewBox="0 0 24 24" aria-hidden="true">
            <path fill="#fff" d="M6.6 10.8c1.4 2.8 3.8 5.1 6.6 6.6l2.2-2.2c.3-.3.7-.4 1-.2 1.1.4 2.3.6 3.6.6.6 0 1 .4 1 1V20c0 .6-.4 1-1 1C10.6 21 3 13.4 3 4c0-.6.4-1 1-1h3.5c.6 0 1 .4 1 1 0 1.3.2 2.5.6 3.6.1.3 0 .7-.2 1L6.6 10.8z"/>
          </svg>
        </span>
        <span class="label">Contact Number</span>
      </li>
      <li class="contact-item item-email">
        <span class="icon">
          <svg width="24" height="18" viewBox="0 0 24 18" aria-hidden="true">
            <rect x="0.5" y="0.5" width="23" height="17" fill="#fff"/>
            <path d="M1 1l11 9 11-9M1 17l8-7M23 17l-8-7" stroke="#000" stroke-width="1.5" fill="none"/>
          </svg>
        </span>
        <span class="label">Email</span>
      </li>
      <li class="contact-item item-website">
        <span class="icon">
          <svg width="26" height="26" viewBox="0 0 24 24" aria-hidden="true">
            <g fill="none" stroke="#fff" stroke-width="1.6">
              <circle cx="12" cy="12" r="10"/>
              <ellipse cx="12" cy="12" rx="4.5" ry="10"/>
              <path d="M2 12h20M4 6.5h16M4 17.5h16"/>
            </g>
          </svg>
        </span>
        <span class="label">Website</span>
      </li>
      <li class="contact-item item-social-a">
        <span class="icon"><span class="plain-dot"></span></span>
        <span class="label">Friendspace</span>
      </li>
      <li class="contact-item item-social-b">
        <span class="icon"><span class="plain-square"></span></span>
        <span class="label">snapframe</span>
      </li>
    </ul>

    <p class="specialties">Bridal, Glamour, Evening, Editorial<br>Fashion, Tv, Film makeup</p>
  </main>
</body>
</html>
```